Tinker's Fox sports bar beer & food menu

We need a menu design for our gastropub sports bar in L.A.'s Sawtelle Neighborhood (Little Osaka). We have a full-bar (hard liquor, craft beer, wine and cocktails) . We have a lunch and dinner menu as well as a happy hour menu. On Sundays we have a seperate menu with brunch items. The design concept is a British pub type of sports bar. We're looking for something different from our existing menu design. Ideally something cleaner and more legible. It should mesh a simple, modern sensibility with the more traditional darkened pub style of our interior design.

You can check out our Venuvista page for photos of the interior/exterior:
https://www.venuvista.com/biz_photos/tinkers-fox-los-angeles?tab=interior

You can view our existing menu here:
https://www.venuvista.com/biz_photos/tinkers-fox-los-angeles?tab=menu

If there's an area of the design that can be a little more playful it's our highlighted event schedule so that the events will stand out.

Target Market(s)

Age of 25 and up. Sawtelle is a cultural hub that caters to a younger, moderately affluent crowd.

Industry/Entity Type

Sports Bar

Font styles to use
Sans Serif

Colors

Designer to choose colors to be used in the design.

Requirements
Must have
• Logo, highlighted event schedule (beer pong Monday, trivia Tuesday, taco Tuesday, whiskey Wednesday, karaoke Saturday). The menu should be easy to read in a darkened bar. We'll be printing on standard 8.5x11 in portrait.
Nice to have
• We're trying to have the menu take up as few pages as possible.
Should not have
• We're trying to have the menu take up as few pages as possible. Food photography isn't necessary. A cover isn't necessary. Please avoid clip art of food.

```html
<!DOCTYPE html>
<html lang="en">
<head>
<meta charset="utf-8">
<title>Tinker's Fox — Burgers and Sandwiches Menu</title>
<link rel="stylesheet" href="https://fonts.googleapis.com/css2?family=Open+Sans:wght@400;600;700;800&display=swap">
<style>
  :root {
    --backdrop: #dfe3e2;
    --page: #343637;
    --band-light: #f7e21a;
    --band-mid: #fcc20e;
    --band-deep: #f5a81a;
    --pill: #fcc514;
    --ink: #1c1c1c;
    --paper: #ffffff;
    --price: #e0202a;
    --label-text: #f39a12;
    --desc: #f2f2f2;
    --tab: #46494a;
  }
  * { box-sizing: border-box; margin: 0; padding: 0; }
  html, body {
    width: 1200px; height: 1175px; overflow: hidden;
    background: var(--backdrop);
    font-family: "Open Sans", sans-serif;
  }
  .menu-page {
    position: absolute; left: 165px; top: 24px;
    width: 870px; height: 1126px;
    background: var(--page);
    overflow: hidden;
  }
  .brand-band {
    position: absolute; left: 0; top: 70px; width: 100%; height: 150px;
    background: linear-gradient(90deg, var(--band-deep) 0%, var(--band-mid) 30%, var(--band-light) 50%, var(--band-mid) 72%, var(--band-deep) 100%);
    display: flex; align-items: center; justify-content: center; gap: 22px;
  }
  .brand-mark {
    width: 54px; height: 54px; border-radius: 50%;
    background: var(--ink);
  }
  .brand-name {
    font-weight: 700; font-size: 64px; color: var(--ink);
    letter-spacing: 1px; line-height: 1;
  }
  .section-label {
    position: absolute; left: 50%; top: 196px; transform: translateX(-50%);
    background: var(--paper);
    padding: 8px 26px;
    font-weight: 800; font-size: 26px; color: var(--label-text);
    letter-spacing: 0.5px; white-space: nowrap;
    box-shadow: 0 6px 10px rgba(0,0,0,.45);
  }
  .menu-list {
    position: absolute; left: 0; top: 270px; width: 100%;
    list-style: none;
    display: flex; flex-direction: column; align-items: center; gap: 10px;
  }
  .menu-item { display: flex; flex-direction: column; align-items: center; }
  .item-bar {
    position: relative;
    width: 380px; height: 32px;
    background: var(--pill);
    border-radius: 16px;
    display: flex; align-items: center; justify-content: center;
    box-shadow: 0 4px 6px rgba(0,0,0,.4);
  }
  .item-name {
    font-weight: 800; font-size: 19px; color: var(--ink);
    margin-right: 40px;
  }
  .item-price {
    position: absolute; right: 14px; top: 50%; transform: translateY(-50%);
    background: var(--paper); color: var(--price);
    font-weight: 800; font-size: 19px;
    border: 2px solid var(--ink);
    border-radius: 14px; padding: 0 9px; line-height: 26px;
  }
  .item-desc {
    margin-top: 5px;
    font-size: 15px; font-weight: 400; color: var(--desc);
    text-align: center; line-height: 1.35; max-width: 560px;
  }
  .page-number {
    position: absolute; right: 0; bottom: 110px;
    width: 84px; height: 46px;
    background: var(--tab);
    clip-path: polygon(18px 0, 100% 0, 100% 100%, 18px 100%, 0 50%);
    color: var(--paper); font-weight: 800; font-size: 20px;
    display: flex; align-items: center; justify-content: center; padding-left: 10px;
  }
</style>
</head>
<body>
  <main class="menu-page">
    <header class="brand-band">
      <span class="brand-mark" aria-hidden="true"></span>
      <h1 class="brand-name">Tinker's Fox</h1>
    </header>

    <h2 class="section-label">BURGERS AND SANDWICHES</h2>

    <ul class="menu-list">
      <li class="menu-item">
        <div class="item-bar"><span class="item-name">Chicken Sandwich</span><span class="item-price">$12</span></div>
        <p class="item-desc">Chicken Breast, Applewood Bacon, Butter Lettuce, White Cheddar, Avocado and<br>Tomato Served on Sourdough Bread</p>
      </li>
      <li class="menu-item">
        <div class="item-bar"><span class="item-name">Buttermilk Fried Chicken</span><span class="item-price">$13</span></div>
        <p class="item-desc">Coleslaw, Provolone, Tomato, and a Spiced Mayonnaise on a Pretzel Roll</p>
      </li>
      <li class="menu-item">
        <div class="item-bar"><span class="item-name">Short Rib Sandwich</span><span class="item-price">$13</span></div>
        <p class="item-desc">Beef Shorts, Mayo, Tomato, Caramelized Onions, Arugula, Pepper Jack Cheese<br>Served on Sourdough Bread</p>
      </li>
      <li class="menu-item">
        <div class="item-bar"><span class="item-name">Grilled Cheese Sandwich</span><span class="item-price">$10</span></div>
        <p class="item-desc">Cheese, Provolone and Cheddar Cheese</p>
      </li>
      <li class="menu-item">
        <div class="item-bar"><span class="item-name">Tinker's Fox Burger</span><span class="item-price">$14</span></div>
        <p class="item-desc">Sharp Cheddar, Arugula, Roasted Shallots, Bacon Jam with Malt Aioli</p>
      </li>
      <li class="menu-item">
        <div class="item-bar"><span class="item-name">The Truffle Burger</span><span class="item-price">$15</span></div>
        <p class="item-desc">Caramelized Onions, Arugula, Truffle Pecorino, Truffle Mayo and Truffle Fries</p>
      </li>
      <li class="menu-item">
        <div class="item-bar"><span class="item-name">The Sloppy Joe</span><span class="item-price">$10</span></div>
        <p class="item-desc">Shredded Lettuce and Sharp Cheddar</p>
      </li>
      <li class="menu-item">
        <div class="item-bar"><span class="item-name">Veggie Burger</span><span class="item-price">$12</span></div>
        <p class="item-desc">Concoction of kale, Tomato, Avocado, Sharp Cheddar with a Balsamic Reduction</p>
      </li>
      <li class="menu-item">
        <div class="item-bar"><span class="item-name">Flat Iron Steak Sandwich</span><span class="item-price">$16</span></div>
        <p class="item-desc">Arugula, Peppers, Fontina, Onion and Mayo</p>
      </li>
      <li class="menu-item">
        <div class="item-bar"><span class="item-name">Chicken Spinach Wrap</span><span class="item-price">$10</span></div>
        <p class="item-desc">Chicken, Bacon, Lettuce, Tomato, Avocado, Ranch and Mayo</p>
      </li>
      <li class="menu-item">
        <div class="item-bar"><span class="item-name">Fried Chicken Sliders (4)</span><span class="item-price">$12</span></div>
        <p class="item-desc">Coleslaw, Lime Sriracha Sauce</p>
      </li>
    </ul>

    <div class="page-number">01</div>
  </main>
</body>
</html>
```